Design für Eisverpackung
Zielgruppe
Wir sind ein kleiner regionaler Eisproduzent, betreiben ein Eiscafe mit eigener Produktion. Wir füllen unsere Produkte in Plaste- bzw. Hartpapierbechern ab und vermarkten sie im Einzelhandel, Tankstellen und zu Festen aller Art. Wir benötigen für eine neue Eisverpackung ein ansprechendes und modernes Design.
Aufgabenstellung
Bei der neuen Verpackungseinheit handelt es sich um einen 130ml Hartpapierbecher (Foto Anhang).
Die Designgestaltung umfasst den Becher und ein Rundetikett, welches auf den Becherdeckel platziert wird. Der Becherdeckel selber bleibt neutral weiß,er soll nur mit dem Rundetikett (Durchmesser ca. 6cm) beklebt werden. Eine Skizze als Designvorlage (Becher) finden Sie im Anhang unten. Das Design soll ein hochwertiges Produkt wieder spiegeln.
Bei der Gestaltung des Bechers haben wir schon konkrete Vorstellungen. Der Becher sollte Eissorten-neutral gestaltet werden, da er bei der Verpackung verschiedener Geschmacksrichtungen Anwendung findet.
Des weiteren die Einarbeitung unseres Logo´s (Anhang), der Name des Produktes ("Süßer Moment")und die Bezeichnung Milcheis. Farblich soll der Becher die Farben Hellblau als Grundfarbe und Gelb haben. Der Name " Süßer Moment" vielleicht in rot.
Es müssen auf der Becherrückseite Freiflächen berücksichtigt werden, auf denen wir Informationen wie Inhaltsstoffe und Nährwerte etc. platzieren können.
Die Deckelgestaltung soll im Design natürlich harmonisch zum Gesamtbecher passen.
Zu berücksichtigen ist lediglich, das auf dem Deckel eine Freifläche vorhanden seien muss,
auf der die entsprechende Eissorte Platz findet. Diese wird von uns per Thermodruck entsprechend auf das Deckeletikett platziert.

```html
<!DOCTYPE html>
<html lang="de">
<head>
<meta charset="utf-8">
<title>Süßer Moment – Milcheis Verpackung</title>
<link href="https://fonts.googleapis.com/css2?family=Lobster&family=Nunito:wght@400;800&display=swap" rel="stylesheet">
<style>
  :root {
    --sky: #7ccbe6;
    --sky-light: #d9f0f8;
    --cream: #fff6dc;
    --sun: #fbc42c;
    --orange: #f08a1c;
    --red: #c8161d;
    --milk-blue: #1f5fa8;
    --ink: #555555;
    --white: #ffffff;
  }
  html, body {
    margin: 0;
    width: 1200px;
    height: 848px;
    overflow: hidden;
    background: var(--white);
  }
  .canvas {
    position: relative;
    width: 1200px;
    height: 848px;
  }

  /* ---------- lid label ---------- */
  .lid-label {
    position: absolute;
    left: 80px;
    top: 184px;
    width: 480px;
    height: 480px;
    border-radius: 50%;
    background: radial-gradient(circle, var(--white) 62%, var(--sky) 100%);
  }
  .lid-label__face {
    position: absolute;
    inset: 28px;
    border-radius: 50%;
    overflow: hidden;
    border: 3px solid var(--white);
    background:
      radial-gradient(ellipse 70% 45% at 50% 35%, var(--white) 0%, rgba(255,255,255,0) 100%),
      linear-gradient(180deg, var(--sky) 0%, var(--sky-light) 35%, var(--cream) 62%, var(--sun) 85%, var(--orange) 100%);
  }
  .splash {
    position: absolute;
    border-radius: 50% 50% 40% 40%;
    background: radial-gradient(ellipse at 50% 40%, #ffffff 0%, #f2f4f6 60%, rgba(255,255,255,0) 100%);
  }
  .lid-label .splash { left: 40px; right: 40px; top: 190px; height: 240px; }

  .brand {
    position: absolute;
    left: 0; right: 0;
    text-align: center;
    font-family: 'Nunito', sans-serif;
  }
  .brand__name {
    font-weight: 800;
    color: var(--milk-blue);
  }
  .brand__dot {
    display: inline-block;
    border-radius: 50%;
    background: var(--sky);
    vertical-align: middle;
    margin-right: 5px;
  }
  .brand__claim {
    display: block;
    font-weight: 400;
    color: var(--ink);
    letter-spacing: 1px;
  }
  .lid-label .brand { top: 62px; }
  .lid-label .brand__name { font-size: 19px; }
  .lid-label .brand__dot { width: 12px; height: 12px; }
  .lid-label .brand__claim { font-size: 8px; }

  .title {
    position: absolute;
    margin: 0;
    font-family: 'Lobster', cursive;
    font-weight: 400;
    color: var(--red);
    line-height: 0.85;
    transform: rotate(-6deg);
    text-shadow: 2px 2px 0 var(--white), 4px 4px 3px rgba(0,0,0,0.25);
    text-align: center;
  }
  .title__top, .title__main { display: block; }
  .lid-label .title { left: 40px; right: 30px; top: 112px; }
  .lid-label .title__top { font-size: 64px; padding-left: 50px; }
  .lid-label .title__main { font-size: 82px; }

  .product-type {
    position: absolute;
    font-family: 'Lobster', cursive;
    color: var(--white);
    -webkit-text-stroke: 1.5px var(--milk-blue);
    transform: rotate(-8deg);
  }
  .lid-label .product-type { right: 52px; top: 250px; font-size: 46px; }

  .ribbon {
    position: absolute;
    background: linear-gradient(90deg, var(--sun) 0%, #b8731f 40%, var(--sun) 75%, #f5b82a 100%);
    transform: rotate(-8deg);
    font-family: 'Lobster', cursive;
    color: var(--white);
    text-align: center;
  }
  .lid-label .ribbon {
    left: 66px; width: 296px; top: 322px;
    height: 48px; line-height: 52px; font-size: 38px;
  }
  .lid-label .ribbon--free { background: linear-gradient(90deg, rgba(251,196,44,0.9), rgba(240,138,28,0.9)); }

  .spoon-note {
    position: absolute;
    font-family: 'Lobster', cursive;
    color: var(--red);
    transform: rotate(-8deg);
  }
  .lid-label .spoon-note { left: 0; right: 0; text-align: center; top: 372px; font-size: 20px; padding-left: 40px; }

  /* ---------- cup wrap ---------- */
  .cup-wrap {
    position: absolute;
    left: 560px;
    top: 250px;
    width: 640px;
    height: 400px;
  }
  .cup-wrap svg { position: absolute; left: 0; top: 0; }
  .cup-wrap .splash { left: 150px; width: 340px; top: 170px; height: 180px; }
  .cup-wrap .brand { top: 52px; }
  .cup-wrap .brand__name { font-size: 13px; }
  .cup-wrap .brand__dot { width: 8px; height: 8px; }
  .cup-wrap .brand__claim { font-size: 6px; }
  .cup-wrap .title { left: 180px; width: 290px; top: 92px; }
  .cup-wrap .title__top { font-size: 40px; padding-left: 40px; }
  .cup-wrap .title__main { font-size: 50px; }
  .cup-wrap .product-type { left: 328px; top: 184px; font-size: 30px; -webkit-text-stroke: 1px var(--milk-blue); }
  .cup-wrap .ribbon {
    left: 230px; width: 170px; top: 230px;
    height: 28px; line-height: 31px; font-size: 21px;
  }
  .cup-wrap .spoon-note { left: 300px; top: 262px; font-size: 13px; }
  .imprint {
    position: absolute;
    left: 96px;
    top: 110px;
    font-family: 'Nunito', sans-serif;
    font-size: 5px;
    color: var(--ink);
    transform-origin: left top;
    transform: rotate(84deg);
    white-space: nowrap;
  }
</style>
</head>
<body>
<main class="canvas">

  <section class="lid-label" aria-label="Rundetikett Deckel">
    <div class="lid-label__face">
      <div class="splash" role="img" aria-label="Spritzende Milch"></div>
      <div class="brand">
        <span class="brand__name"><span class="brand__dot"></span>Talwiese</span>
        <span class="brand__claim">frisch aus der Region</span>
      </div>
      <h1 class="title"><span class="title__top">Süßer</span><span class="title__main">Moment</span></h1>
      <div class="product-type">Milcheis</div>
      <div class="ribbon ribbon--free">Vanilla</div>
      <div class="spoon-note">mit Eislöffel</div>
    </div>
  </section>

  <section class="cup-wrap" aria-label="Becherbanderole">
    <svg width="640" height="400" viewBox="0 0 640 400">
      <defs>
        <linearGradient id="wrapSky" x1="0" y1="0" x2="0" y2="1">
          <stop offset="0" stop-color="#7ccbe6"/>
          <stop offset="0.35" stop-color="#e6f5fb"/>
          <stop offset="0.65" stop-color="#fff6dc"/>
          <stop offset="0.85" stop-color="#fbc42c"/>
          <stop offset="1" stop-color="#f08a1c"/>
        </linearGradient>
      </defs>
      <path class="cup-wrap__shape" d="M70,40 Q330,0 590,40 L540,370 Q330,340 120,370 Z" fill="url(#wrapSky)"/>
      <line x1="10" y1="20" x2="80" y2="385" stroke="#555" stroke-width="1" stroke-dasharray="2 2"/>
      <line x1="630" y1="20" x2="560" y2="385" stroke="#555" stroke-width="1" stroke-dasharray="2 2"/>
    </svg>
    <div class="splash" role="img" aria-label="Spritzende Milch"></div>
    <div class="brand">
      <span class="brand__name"><span class="brand__dot"></span>Talwiese</span>
      <span class="brand__claim">frisch aus der Region</span>
    </div>
    <h2 class="title"><span class="title__top">Süßer</span><span class="title__main">Moment</span></h2>
    <div class="product-type">Milcheis</div>
    <div class="ribbon">hmm… lecker</div>
    <div class="spoon-note">mit Eislöffel</div>
    <div class="imprint">Talwiese-Eis | 00000 Beispielort | Am Markt 1</div>
  </section>

</main>
</body>
</html>
```